Executive Headhunting and Recruitment Business

Looking for a website for an executive recruitment and headhunting business based in the UK. We provide headhunting services to the recruitment sector.

I'm pretty open to ideas as long as the website stands out but in a professional way. We are not a budget business, the service we provide is definitely not the cheapest but we are the best at what we do, our value is in our service and we are a high-end business aiming at companies who want to pay for the service they receive so our website should reflect this.

Website should be professional and clean looking.
Updates

Logo now added to Files. Added Saturday, February 13, 2016

Target Market(s)

Recruitment Agencies

Industry/Entity Type

Business

Coding

Coded - Design and coding required

Number of Pages Required

4 page

Requirements
Must have
• Home Page - Current Vacancies - About us - Contact Us
• Clean - Modern - Professional
Nice to have
• Open to ideas.

```html
<!DOCTYPE html>
<html lang="en">
<head>
<meta charset="utf-8">
<title>Ashcombe Reed – Executive Recruitment &amp; Headhunting</title>
<link href="https://fonts.googleapis.com/css2?family=Open+Sans:wght@400;600;700&family=Cinzel:wght@400;700&display=swap" rel="stylesheet">
<style>
:root{
  --navy:#0f2c5a;
  --blue:#1e5fb3;
  --blue-mid:#2b6fc2;
  --blue-light:#bcd6ee;
  --text:#555b63;
  --muted:#8a9098;
  --line:#dfe3e8;
  --band:#eeeff1;
  --footer:#f6f6f7;
  --accent:#d4782e;
  --white:#ffffff;
}
*{margin:0;padding:0;box-sizing:border-box}
html,body{width:1200px;height:2260px;overflow:hidden}
body{position:relative;background:var(--white);font-family:"Open Sans",Arial,sans-serif;color:var(--text)}
.abs{position:absolute}

/* header */
.site-header{left:0;top:0;width:1200px;height:72px;background:var(--white)}
.brand{left:72px;top:14px;display:flex;align-items:center;gap:12px}
.brand-mark{width:44px;height:44px;background:var(--navy)}
.brand-name{font-size:20px;font-weight:600;color:var(--navy);letter-spacing:1px;text-transform:uppercase}
.main-nav{right:72px;top:20px;display:flex;align-items:center;gap:26px;font-size:12px;text-transform:uppercase;letter-spacing:1px;color:var(--navy)}
.main-nav .active{background:var(--navy);color:var(--white);padding:7px 18px;border-radius:14px 0 14px 0}
.nav-phone{display:flex;align-items:center;gap:7px;font-weight:700;font-size:13px;letter-spacing:0}

/* hero */
.hero{left:0;top:72px;width:1200px;height:488px;background:linear-gradient(100deg,#0b3a7e 0%,#1756a6 38%,#4a8bcd 68%,#c6dcf0 100%)}
.hero-title{left:72px;top:166px;width:460px;font-size:34px;line-height:44px;font-weight:700;color:var(--white)}
.hero-dots{left:72px;top:388px;display:flex;gap:8px}
.hero-dots span{width:9px;height:9px;background:rgba(255,255,255,.5)}
.hero-dots span:first-child{background:var(--white)}

/* welcome */
.section-title{font-size:23px;font-weight:600;color:var(--blue);text-transform:uppercase;letter-spacing:.5px}
.welcome{left:72px;top:596px;width:1056px}
.welcome p{margin-top:14px;font-size:13px;line-height:22px}
.btn{display:inline-block;background:var(--navy);color:var(--white);font-size:11px;font-weight:700;text-transform:uppercase;letter-spacing:.5px}
.welcome .btn{margin-top:22px;padding:11px 22px}

/* services band */
.services{left:0;top:790px;width:1200px;height:440px;background:linear-gradient(180deg,#2a2d33 0%,#15171b 60%,#22252b 100%);clip-path:polygon(0 70px,100% 0,100% 370px,0 100%)}
.service{top:920px;width:280px;text-align:center}
.service-icon{width:104px;height:104px;margin:0 auto;border-radius:50%;background:var(--blue-mid);border:4px solid rgba(255,255,255,.25);display:flex;align-items:center;justify-content:center}
.service h3{margin-top:22px;font-family:"Cinzel",Georgia,serif;font-weight:400;font-size:17px;color:var(--white);text-transform:uppercase}
.service p{margin-top:10px;font-size:12px;line-height:19px;color:#c9ccd1}

/* vacancies */
.vacancies{left:72px;top:1290px;width:600px}
.job-table{margin-top:18px;width:100%;border-collapse:collapse;font-size:12px}
.job-table th{text-align:left;font-weight:700;color:var(--navy);padding:10px 8px;border-bottom:2px solid var(--line)}
.job-table td{padding:10px 8px;border-bottom:1px solid var(--line);vertical-align:middle;height:58px}
.job-title{color:var(--blue);font-weight:600}
.job-sub{display:block;font-size:10px;color:var(--muted)}
.job-table .btn{padding:7px 14px;font-size:10px}

/* blog */
.blog{left:704px;top:1290px;width:424px}
.post{display:flex;gap:16px;margin-top:22px}
.post-thumb{flex:0 0 120px;height:88px}
.post p{font-size:12px;line-height:19px}
.post .read{display:block;margin-top:5px;font-size:11px;font-weight:700;color:var(--navy);text-transform:uppercase}

/* press */
.press{left:0;top:1710px;width:1200px;height:210px;background:var(--band)}
.press h2{position:absolute;top:46px;width:100%;text-align:center;font-family:"Cinzel",Georgia,serif;font-weight:400;font-size:26px;color:var(--navy)}
.press-row{position:absolute;top:120px;left:0;width:100%;display:flex;justify-content:center;align-items:center;gap:44px}
.press-row span{height:22px;background:#7b8088;border-radius:3px}

/* footer */
.site-footer{left:0;top:1920px;width:1200px;height:272px;background:var(--footer);border-top:1px solid var(--line)}
.footer-col{top:52px}
.footer-col h4{font-size:13px;font-weight:700;color:var(--accent);text-transform:uppercase;letter-spacing:.5px;margin-bottom:14px}
.footer-col p,.footer-col li{font-size:12px;line-height:21px;list-style:none}
.socials{display:flex;gap:8px}
.socials span{width:30px;height:30px;border-radius:50%;border:1.5px solid #9aa0a8}
.copyright{left:0;top:2192px;width:1200px;height:68px;background:var(--navy);color:#c8d2e2;font-size:11px;display:flex;align-items:center;justify-content:center}
</style>
</head>
<body>

<header class="site-header abs">
  <div class="brand abs"><span class="brand-mark"></span><span class="brand-name">Ashcombe Reed</span></div>
  <nav class="main-nav abs">
    <span class="active">Home</span>
    <span>Current Vacancies</span>
    <span>About Us</span>
    <span>Blog</span>
    <span>Contact Us</span>
    <span class="nav-phone">
      <svg width="14" height="14" viewBox="0 0 24 24"><path fill="#0f2c5a" d="M6.6 10.8a15 15 0 0 0 6.6 6.6l2.2-2.2c.3-.3.7-.4 1-.2 1.1.4 2.3.6 3.6.6.6 0 1 .4 1 1V20c0 .6-.4 1-1 1A17 17 0 0 1 3 4c0-.6.4-1 1-1h3.5c.6 0 1 .4 1 1 0 1.3.2 2.5.6 3.6.1.3 0 .7-.2 1z"/></svg>
      1-800-555-0142
    </span>
  </nav>
</header>

<section class="hero abs" role="img" aria-label="Photo of a businessman holding small executive figures above his open hand, in blue tones">
  <h1 class="hero-title abs">We are an Executive Recruitment &amp; Headhunting Business Based in the UK.</h1>
  <div class="hero-dots abs"><span></span><span></span><span></span><span></span></div>
</section>

<section class="welcome abs">
  <h2 class="section-title">Welcome to our website</h2>
  <p>Aliquam molestie, mi et imperdiet euismod, dui purus auctor tellus, et interdum lacus lectus at ante. Sed accumsan sollicitudin sapien, sit amet adipiscing turpis gravida ac. In congue, neque ac lobortis volutpat, libero mauris varius mi, vitae suscipit ipsum ligula vitae risus. Duis aliquam nibh a dui iaculis viverra id a nulla. Vivamus egestas risus in magna varius commodo. Sed semper viverra egestas. Etiam pretium porttitor lectus, vel ornare neque porta volutpat.</p>
  <span class="btn">Read more</span>
</section>

<section class="services abs" role="img" aria-label="Dark photo of business people silhouettes walking"></section>

<div class="service abs" style="left:160px">
  <div class="service-icon">
    <svg width="50" height="44" viewBox="0 0 50 44"><circle cx="25" cy="12" r="8" fill="#fff"/><path d="M10 42c0-10 7-16 15-16s15 6 15 16z" fill="#fff"/><circle cx="9" cy="16" r="5" fill="#fff" opacity=".7"/><circle cx="41" cy="16" r="5" fill="#fff" opacity=".7"/></svg>
  </div>
  <h3>Employment Recruitment</h3>
  <p>Aliquam molestie, mi et imperdiet euismod, dui purus auctor tellus, et interdum lacus lectus at ante.</p>
</div>
<div class="service abs" style="left:460px">
  <div class="service-icon">
    <svg width="48" height="42" viewBox="0 0 48 42"><rect x="16" y="2" width="16" height="8" fill="none" stroke="#fff" stroke-width="3"/><rect x="2" y="10" width="44" height="30" rx="3" fill="#fff"/><rect x="2" y="22" width="44" height="3" fill="#2b6fc2"/></svg>
  </div>
  <h3>Headhunting Business</h3>
  <p>Aliquam molestie, mi et imperdiet euismod, dui purus auctor tellus, et interdum lacus lectus at ante.</p>
</div>
<div class="service abs" style="left:760px">
  <div class="service-icon">
    <svg width="46" height="42" viewBox="0 0 46 42"><rect x="4" y="26" width="8" height="14" fill="#fff"/><rect x="16" y="18" width="8" height="22" fill="#fff"/><rect x="28" y="10" width="8" height="30" fill="#fff"/><path d="M4 18 16 8l10 6L42 2" fill="none" stroke="#fff" stroke-width="3"/></svg>
  </div>
  <h3>Our Values</h3>
  <p>Aliquam molestie, mi et imperdiet euismod, dui purus auctor tellus, et interdum lacus lectus at ante.</p>
</div>

<section class="vacancies abs">
  <h2 class="section-title">Current Vacancies</h2>
  <table class="job-table">
    <thead><tr><th>Job Title</th><th>Exp Req.</th><th>No. of Post</th><th></th></tr></thead>
    <tbody>
      <tr><td><span class="job-title">Vestibulum ante ipsum</span><span class="job-sub">Duis aliquam nibh</span></td><td><span class="job-title">3yrs - 8yrs</span><span class="job-sub">Duis aliquam nibh</span></td><td>3Nos.</td><td><span class="btn">Apply Now</span></td></tr>
      <tr><td><span class="job-title">Vestibulum ante ipsum</span><span class="job-sub">Duis aliquam nibh</span></td><td><span class="job-title">3yrs - 8yrs</span><span class="job-sub">Duis aliquam nibh</span></td><td>3Nos.</td><td><span class="btn">Apply Now</span></td></tr>
      <tr><td><span class="job-title">Vestibulum ante ipsum</span><span class="job-sub">Duis aliquam nibh</span></td><td><span class="job-title">3yrs - 8yrs</span><span class="job-sub">Duis aliquam nibh</span></td><td>3Nos.</td><td><span class="btn">Apply Now</span></td></tr>
      <tr><td><span class="job-title">Vestibulum ante ipsum</span><span class="job-sub">Duis aliquam nibh</span></td><td><span class="job-title">3yrs - 8yrs</span><span class="job-sub">Duis aliquam nibh</span></td><td>3Nos.</td><td><span class="btn">Apply Now</span></td></tr>
      <tr><td><span class="job-title">Vestibulum ante ipsum</span><span class="job-sub">Duis aliquam nibh</span></td><td><span class="job-title">3yrs - 8yrs</span><span class="job-sub">Duis aliquam nibh</span></td><td>3Nos.</td><td><span class="btn">Apply Now</span></td></tr>
    </tbody>
  </table>
</section>

<section class="blog abs">
  <h2 class="section-title">Blog Posts</h2>
  <article class="post">
    <div class="post-thumb" role="img" aria-label="Photo of a business meeting" style="background:linear-gradient(135deg,#5a6f8c,#c9d3df)"></div>
    <div><p>Aliquam molestie, mi et imperdiet euismod, dui purus auctor tellus, et interdum lacus lectus at ante.</p><span class="read">Read more</span></div>
  </article>
  <article class="post">
    <div class="post-thumb" role="img" aria-label="Photo of a handshake over a desk" style="background:linear-gradient(135deg,#2f4a6e,#8fa6c2)"></div>
    <div><p>Aliquam molestie, mi et imperdiet euismod, dui purus auctor tellus, et interdum lacus lectus at ante.</p><span class="read">Read more</span></div>
  </article>
  <article class="post">
    <div class="post-thumb" role="img" aria-label="Photo of a team working at a table" style="background:linear-gradient(135deg,#1f5aa6,#9cc0e6)"></div>
    <div><p>Aliquam molestie, mi et imperdiet euismod, dui purus auctor tellus, et interdum lacus lectus at ante.</p><span class="read">Read more</span></div>
  </article>
</section>

<section class="press abs">
  <h2>As seen on</h2>
  <div class="press-row">
    <span style="width:110px"></span>
    <span style="width:84px"></span>
    <span style="width:30px;height:30px;border-radius:50%"></span>
    <span style="width:130px"></span>
    <span style="width:110px"></span>
    <span style="width:150px"></span>
  </div>
</section>

<footer class="site-footer abs">
  <div class="footer-col abs" style="left:72px;width:320px">
    <h4>About Ashcombe Reed</h4>
    <p>Aliquam molestie, mi et imperdiet euismod, dui purus auctor tellus, et interdum lacus lectus at ante. Sed accumsan sollicitudin sapien, sit amet adipiscing turpis gravida ac.</p>
  </div>
  <div class="footer-col abs" style="left:452px">
    <h4>Company</h4>
    <ul><li>Home</li><li>Current Vacancies</li><li>About Us</li><li>Blog</li><li>Contact Us</li></ul>
  </div>
  <div class="footer-col abs" style="left:672px">
    <h4>Recent Posts</h4>
    <ul><li>Lorem ipsum dolor sit amet</li><li>Duis aliquam nibh</li><li>Phasellus nisi</li><li>Suspendisse lobortis mauris</li></ul>
  </div>
  <div class="footer-col abs" style="left:884px">
    <h4>Contact Us</h4>
    <div class="socials"><span></span><span></span><span></span><span></span><span></span></div>
  </div>
</footer>

<div class="copyright abs">Copyright © 2016 Company Name All Rights Reserved</div>

</body>
</html>
```